Solar Energy Company Flyer/Door Hanger

Hello designers,

We are a solar energy company looking to make an eye-catching design for residential door hangers. These will be the type of door hangers that just stick to the door, not actually hang on the door. So essentially it will be a flyer that is 5.5" x 8.5" front and back. Please see attached template design for specifications and standards for print. The file will need to be provided in an editable PSD format.

Content for Flyer:

Front: Should be something eye caching, attention grabber, with big words and a visual of something to do with a nice looking home that has solar panels on it. Call to action should be at the bottom.

Words should ready: MAKE CENTS OUT OF SOLAR

Call to action link: apply.brivenpower.net

Back: Should have more in depth content. Company logo on back, 4 bullet points (checkmarks) with text, a chart (attached), and contact info at bottom. We will update content for the back soon, but please put together a layout that doesn't look plain jane and has some creativeness to it.

Update on content will be soon. If you want you can submit the front first and the back after.

Thanks!

Target Market(s)

Residential Home Owners

Industry/Entity Type

Solar Energy

Requirements
Must have
• Front should be clean and eycatching, back should be creative yet informational

```html
<!DOCTYPE html>
<html lang="en">
<head>
<meta charset="utf-8">
<title>Briven Home Solar – Door Hanger Front</title>
<link rel="stylesheet" href="https://fonts.googleapis.com/css2?family=Oswald:wght@400;600&family=Lato:wght@400;700&display=swap">
<style>
  :root {
    --orange: #ee6a1f;
    --orange-dark: #d9561a;
    --grey: #6d6d6d;
    --grey-band: #7a7a7a;
    --ink: #1c1c1c;
    --white: #ffffff;
    --page: #ffffff;
    --sky-top: #3f7fd8;
    --sky-mid: #6fa3e6;
    --panel: #2c4f9c;
  }
  html, body {
    margin: 0;
    padding: 0;
    width: 1200px;
    height: 1200px;
    overflow: hidden;
    background: var(--page);
  }
  .flyer {
    position: absolute;
    left: 240px;
    top: 36px;
    width: 720px;
    height: 1128px;
    background: var(--white);
    overflow: hidden;
  }
  .flyer-art {
    position: absolute;
    inset: 0;
    width: 720px;
    height: 1128px;
  }
  .brand-name {
    font-family: "Lato", sans-serif;
    font-weight: 700;
    fill: var(--ink);
  }
  .headline-strong {
    font-family: "Oswald", sans-serif;
    font-weight: 600;
    fill: var(--orange);
  }
  .headline-light {
    font-family: "Oswald", sans-serif;
    font-weight: 400;
    fill: var(--grey);
  }
  .cta-text {
    font-family: "Lato", sans-serif;
    font-weight: 700;
    fill: var(--white);
  }
</style>
</head>
<body>
<div class="flyer">
  <svg class="flyer-art" viewBox="0 0 720 1128" xmlns="http://www.w3.org/2000/svg">
    <defs>
      <linearGradient id="roofPhotoTone" x1="0" y1="0" x2="0" y2="1">
        <stop offset="0" stop-color="#e9f1fb"/>
        <stop offset="0.12" stop-color="var(--sky-mid)"/>
        <stop offset="0.45" stop-color="var(--sky-top)"/>
        <stop offset="0.65" stop-color="#5b6f95"/>
        <stop offset="1" stop-color="var(--panel)"/>
      </linearGradient>
      <radialGradient id="insetTone" cx="0.5" cy="0.55" r="0.6">
        <stop offset="0" stop-color="#f4f5f8"/>
        <stop offset="0.6" stop-color="#b9bccb"/>
        <stop offset="1" stop-color="#7d8196"/>
      </radialGradient>
      <linearGradient id="fieldTone" x1="0" y1="0" x2="0" y2="1">
        <stop offset="0" stop-color="#ffffff"/>
        <stop offset="1" stop-color="#cfcfcf"/>
      </linearGradient>
    </defs>

    <!-- hero photo area -->
    <path role="img" aria-label="Photo of three installers fitting solar panels on a rooftop under a blue sky"
          d="M0,0 L342,0 Q420,232 720,262 L720,532 Q270,520 0,700 Z"
          fill="url(#roofPhotoTone)"/>

    <!-- top-right arc -->
    <path d="M342,0 Q420,232 720,262" fill="none" stroke="var(--orange)" stroke-width="4"/>

    <!-- brand name -->
    <text class="brand-name" x="690" y="118" font-size="34" text-anchor="end">Briven Home Solar</text>

    <!-- curved bands -->
    <path d="M0,700 Q270,520 720,532 L720,556 Q300,556 0,724 Z" fill="var(--orange)"/>
    <path d="M0,742 Q290,578 720,568 L720,590 Q310,604 0,780 Z" fill="var(--grey-band)"/>

    <!-- faded panel field at bottom -->
    <rect role="img" aria-label="Faded photo of a solar panel field" x="0" y="900" width="720" height="228" fill="url(#fieldTone)"/>

    <!-- inset circle -->
    <circle cx="229" cy="610" r="132" fill="var(--white)"/>
    <circle cx="229" cy="610" r="126" fill="var(--orange)"/>
    <circle role="img" aria-label="Illustration of the Earth beside a solar panel and a wind turbine" cx="229" cy="610" r="118" fill="url(#insetTone)"/>

    <!-- headline -->
    <text class="headline-strong" x="58" y="876" font-size="142" textLength="612" lengthAdjust="spacingAndGlyphs">MAKE CENTS</text>
    <text class="headline-light" x="56" y="984" font-size="100" textLength="614" lengthAdjust="spacingAndGlyphs">OUT OF SOLAR</text>

    <!-- call to action -->
    <rect x="56" y="1006" width="626" height="54" rx="16" fill="var(--orange)" stroke="var(--orange-dark)" stroke-width="1.5"/>
    <text class="cta-text" x="369" y="1045" font-size="35" text-anchor="middle">Visit us:  apply.brivenpower.net</text>
  </svg>
</div>
</body>
</html>
```